Supply Chain Management Site - CrateLoomHQ

We are a supply chain management company that offers the following products:
Warehouse Management System (WMS)
Order Management System (OMS)
Delivery / Fleet Management System

Our product caters to 3PL and distributions.

Ideally a site with a light background would be good.
We like the following sites:
www.quintarel.com
http://www.bravelmo.com/us/
http://www.tirevka.com/

You can use the content from here:
http://host.sampleyard874.com/demo/crateloom-hq/

However, we really DO NOT like the design. You DO NOT have to have all the content on the home page. We can have the features and other things on other pages.

```html
<!DOCTYPE html>
<html lang="en">
<head>
<meta charset="utf-8">
<title>CrateLoom HQ – Warehouse Management</title>
<link rel="stylesheet" href="https://fonts.googleapis.com/css2?family=Raleway:wght@400;500;600&family=Open+Sans:wght@400;600&display=swap">
<style>
:root{
  --brand-blue:#1e7fb5;
  --accent-orange:#f39c12;
  --hero-orange:#f6a800;
  --hero-blue:#1f5d8c;
  --cyan:#1ba3d6;
  --button-cyan:#14a9e3;
  --ink:#333;
  --muted:#8a8a8a;
  --soft-bg:#f4f4f4;
  --line:#e4e4e4;
  --tile-green:#6cb42c;
  --tile-orange:#e09a0e;
  --tile-cyan:#1ea7d8;
  --tile-navy:#21507d;
  --benefit-orange:#e39a1a;
  --footer-bg:#174a6f;
  --footer-bottom:#103c5c;
  --footer-text:#d7e3ee;
  --white:#fff;
}
*{box-sizing:border-box;margin:0;padding:0}
html,body{width:1200px;height:2439px;overflow:hidden}
body{position:relative;background:var(--white);font-family:'Open Sans',sans-serif;color:var(--ink)}
.abs{position:absolute}

/* header */
.site-header{position:absolute;left:0;top:0;width:1200px;height:104px;background:var(--white)}
.brand{left:138px;top:35px}
.brand-name{display:flex;align-items:center;gap:10px;font-family:'Raleway',sans-serif;font-weight:600;font-size:33px;color:var(--brand-blue);line-height:1}
.brand-mark{width:30px;height:30px;border:3px solid var(--brand-blue)}
.main-nav{left:494px;top:46px;display:flex;gap:38px;font-family:'Raleway',sans-serif;font-size:13px;font-weight:500;color:#444;letter-spacing:.3px}
.header-tools{left:854px;top:0;height:104px;display:flex;align-items:center}
.search-btn{width:64px;height:104px;border-left:1px solid var(--line);border-right:1px solid var(--line);display:flex;align-items:center;justify-content:center}
.header-phone{margin-left:18px;display:flex;align-items:center;gap:8px;font-size:15px;color:#333}

/* hero */
.hero{left:0;top:104px;width:1200px;height:514px;overflow:hidden}
.hero-art{position:absolute;inset:0}
.hero-copy{position:absolute;left:0;width:1200px;text-align:center;color:var(--white);font-family:'Raleway',sans-serif}
.hero-title{top:176px;font-size:36px;font-weight:500}
.hero-sub{top:226px;font-size:27px;font-weight:400}
.hero-btn{position:absolute;left:543px;top:275px;width:129px;height:35px;background:var(--button-cyan);color:var(--white);font-size:15px;line-height:35px;text-align:center;font-family:'Open Sans',sans-serif}
.hero-arrow{position:absolute;top:206px}

/* intro */
.intro{left:0;top:618px;width:1200px;height:320px;border-bottom:1px solid var(--line)}
.intro-heading{position:absolute;left:150px;top:80px;font-family:'Raleway',sans-serif;color:#333;font-weight:400}
.intro-heading .line-small{display:block;font-size:29px}
.intro-heading .line-large{display:block;font-size:36px;margin-top:4px}
.intro-text{position:absolute;left:150px;top:170px;width:480px;font-size:11px;line-height:17.5px;color:var(--muted)}
.intro-art{position:absolute;left:699px;top:65px;width:293px;height:211px;border-radius:6px;background:linear-gradient(135deg,#f3f1ec,#e9d7b8 55%,#f0e2a8)}

/* products */
.products{left:0;top:938px;width:1200px;height:332px;background:var(--soft-bg)}
.product{position:absolute;top:80px;width:300px;text-align:center}
.product-icon{height:56px;display:flex;justify-content:center;align-items:flex-end}
.product-title{margin-top:28px;font-family:'Raleway',sans-serif;font-size:20px;line-height:20px;color:#333}
.product-text{margin:10px auto 0;width:260px;font-size:11px;line-height:18px;color:var(--muted)}

/* tiles */
.tiles{left:0;top:1270px;width:1200px;height:476px;display:grid;grid-template-columns:600px 600px;grid-template-rows:238px 238px}
.tile{position:relative;text-align:center;color:var(--white)}
.tile-photo{position:absolute;inset:0}
.tile-green .tile-photo{background:linear-gradient(90deg,#78bd34,var(--tile-green) 60%,#62a826)}
.tile-orange .tile-photo{background:linear-gradient(90deg,#d8920a,var(--tile-orange) 50%,#e8a51c)}
.tile-cyan .tile-photo{background:linear-gradient(90deg,#2aafe0,var(--tile-cyan) 60%,#1795c6)}
.tile-navy .tile-photo{background:linear-gradient(90deg,#1d4770,var(--tile-navy) 50%,#2b5f8c)}
.tile + .tile{border-left:1px solid rgba(255,255,255,.35)}
.tile-hex{position:absolute;left:258px;top:38px}
.tile-title{position:absolute;left:0;right:0;top:140px;font-family:'Raleway',sans-serif;font-size:24px;font-weight:500}
.tile-sub{position:absolute;left:0;right:0;top:176px;font-size:14px}

/* benefits */
.benefits{left:0;top:1746px;width:1200px;height:384px}
.benefit-block{position:absolute;top:68px}
.benefit-heading{font-family:'Raleway',sans-serif;font-size:24px;font-weight:500}
.benefit-heading.orange{color:var(--benefit-orange)}
.benefit-heading.cyan{color:var(--cyan)}
.benefit-photo{position:absolute;top:36px;border-radius:4px}
.benefit-list{position:absolute;list-style:none;font-family:'Raleway',sans-serif;font-size:13.5px;color:#444;line-height:19px}
.benefit-list li{margin-bottom:10px}

/* footer */
.site-footer{left:0;top:2130px;width:1200px;height:247px;background:var(--footer-bg);color:var(--footer-text)}
.footer-col{position:absolute;top:41px}
.footer-col h3{font-family:'Raleway',sans-serif;font-weight:500;font-size:15px;color:var(--white);letter-spacing:.4px;margin-bottom:12px}
.footer-col ul{list-style:none;font-size:12px;line-height:25px;color:var(--white)}
.newsletter-note{font-size:11px;color:var(--footer-text)}
.email-field{margin-top:10px;width:229px;height:30px;background:var(--white);color:#999;font-size:11px;line-height:30px;padding-left:8px}
.subscribe-btn{margin-top:8px;width:112px;height:30px;background:#2bb5e0;color:var(--white);font-size:12px;line-height:30px;text-align:center}
.contact-lines{font-size:12px;line-height:24px;color:var(--white)}
.social{display:flex;gap:14px;margin-top:12px}
.social span{width:22px;height:22px;border-radius:50%;background:var(--white);opacity:.9}
.footer-bottom{left:0;top:2377px;width:1200px;height:62px;background:var(--footer-bottom);color:#9db4c8;font-size:10px}
.footer-bottom p{position:absolute;left:158px;top:27px}
</style>
</head>
<body>

<header class="site-header">
  <div class="brand abs">
    <div class="brand-name"><span class="brand-mark"></span>CrateLoom HQ</div>
  </div>
  <nav class="main-nav abs">
    <span>HOME</span><span>ABOUT US</span><span>FEATURES</span><span>CONTACT</span>
  </nav>
  <div class="header-tools abs">
    <div class="search-btn">
      <svg width="20" height="20" viewBox="0 0 20 20"><circle cx="8" cy="8" r="6" fill="none" stroke="#1f4d75" stroke-width="2.6"/><line x1="12.5" y1="12.5" x2="18" y2="18" stroke="#1f4d75" stroke-width="3" stroke-linecap="round"/></svg>
    </div>
    <div class="header-phone">
      <svg width="18" height="18" viewBox="0 0 24 24"><path d="M6.6 10.8a15.1 15.1 0 0 0 6.6 6.6l2.2-2.2a1 1 0 0 1 1-.25 11.4 11.4 0 0 0 3.6.57 1 1 0 0 1 1 1V20a1 1 0 0 1-1 1A17 17 0 0 1 3 4a1 1 0 0 1 1-1h3.5a1 1 0 0 1 1 1c0 1.25.2 2.45.57 3.57a1 1 0 0 1-.25 1z" fill="#f39c12"/></svg>
      (555) 014-2290
    </div>
  </div>
</header>

<section class="hero abs">
  <svg class="hero-art" role="img" aria-label="Warehouse worker carrying a box on an orange tint beside a manager at a laptop on a blue tint" width="1200" height="514" viewBox="0 0 1200 514">
    <defs>
      <linearGradient id="heroOrange" x1="0" x2="1"><stop offset="0" stop-color="#f7b400"/><stop offset="1" stop-color="#f49d00"/></linearGradient>
      <linearGradient id="heroBlue" x1="0" x2="1"><stop offset="0" stop-color="#245f8d"/><stop offset="1" stop-color="#1b5582"/></linearGradient>
    </defs>
    <rect width="1200" height="514" fill="url(#heroBlue)"/>
    <polygon points="0,0 667,0 524,514 0,514" fill="url(#heroOrange)"/>
  </svg>
  <div class="hero-copy hero-title">Warehouse Management system Should be</div>
  <div class="hero-copy hero-sub">Check out our options and features included</div>
  <div class="hero-btn">Get Started</div>
  <svg class="hero-arrow" style="left:108px" width="24" height="56" viewBox="0 0 24 56"><polyline points="22,2 3,28 22,54" fill="none" stroke="#fff" stroke-width="2"/></svg>
  <svg class="hero-arrow" style="left:1064px" width="24" height="56" viewBox="0 0 24 56"><polyline points="2,2 21,28 2,54" fill="none" stroke="#fff" stroke-width="2"/></svg>
</section>

<section class="intro abs">
  <h1 class="intro-heading"><span class="line-small">What &nbsp;a Warehouse</span><span class="line-large">Management System</span></h1>
  <p class="intro-text">CrateLoom HQ gives warehouse teams one clear view of stock, locations and labor. Receive, put away, pick, pack and ship with fewer errors and faster turns, whether you run a single distribution center or a growing network serving many 3PL clients every day.</p>
  <div class="intro-art" role="img" aria-label="Isometric illustration of a worker with pallet jacks, stacked cartons and warehouse carts"></div>
</section>

<section class="products abs">
  <div class="product" style="left:135px">
    <div class="product-icon">
      <svg width="58" height="52" viewBox="0 0 58 52" fill="var(--cyan)"><rect x="21" y="0" width="16" height="14"/><rect x="2" y="36" width="16" height="14"/><rect x="21" y="36" width="16" height="14"/><rect x="40" y="36" width="16" height="14"/><rect x="27.5" y="14" width="3" height="22"/><rect x="8.5" y="24" width="41" height="3"/><rect x="8.5" y="24" width="3" height="12"/><rect x="46.5" y="24" width="3" height="12"/></svg>
    </div>
    <div class="product-title">Warehouse<br>Management System</div>
    <p class="product-text">Track every pallet, bin and lot in real time across all of your sites and docks.</p>
  </div>
  <div class="product" style="left:448px">
    <div class="product-icon">
      <svg width="86" height="56" viewBox="0 0 86 56"><rect x="10" y="3" width="66" height="44" rx="4" fill="none" stroke="var(--cyan)" stroke-width="5"/><rect x="0" y="49" width="86" height="6" rx="3" fill="var(--cyan)"/></svg>
    </div>
    <div class="product-title">Order<br>Management System</div>
    <p class="product-text">Capture, route and fulfill orders from every channel in one simple screen.</p>
  </div>
  <div class="product" style="left:762px">
    <div class="product-icon">
      <svg width="50" height="50" viewBox="0 0 50 50"><polygon points="48,2 2,20 20,28 28,48" fill="var(--cyan)"/><polyline points="48,2 20,28" stroke="var(--soft-bg)" stroke-width="2.5"/></svg>
    </div>
    <div class="product-title">Delivery / Fleet<br>Management System</div>
    <p class="product-text">Plan routes, dispatch drivers and confirm each delivery with live updates.</p>
  </div>
</section>

<section class="tiles abs">
  <div class="tile tile-green">
    <div class="tile-photo" role="img" aria-label="Businessman reviewing documents, green tint"></div>
    <svg class="tile-hex" width="84" height="94" viewBox="0 0 84 94"><polygon points="42,2 82,24 82,70 42,92 2,70 2,24" fill="#fff"/><circle cx="42" cy="42" r="11" fill="none" stroke="var(--tile-green)" stroke-width="3.5"/><rect x="37" y="53" width="10" height="9" fill="var(--tile-green)"/></svg>
    <div class="tile-title">Strategy</div>
    <div class="tile-sub">Morbi diam mauris viverra in gravida</div>
  </div>
  <div class="tile tile-orange">
    <div class="tile-photo" role="img" aria-label="Hand presenting interlocking gears, orange tint"></div>
    <svg class="tile-hex" width="84" height="94" viewBox="0 0 84 94"><polygon points="42,2 82,24 82,70 42,92 2,70 2,24" fill="#fff"/><g fill="var(--tile-orange)" transform="translate(42 47)"><circle r="11"/><rect x="-3.5" y="-16" width="7" height="32"/><rect x="-16" y="-3.5" width="32" height="7"/><rect x="-3.5" y="-16" width="7" height="32" transform="rotate(45)"/><rect x="-3.5" y="-16" width="7" height="32" transform="rotate(-45)"/><circle r="4.5" fill="#fff"/></g></svg>
    <div class="tile-title">Planning</div>
    <div class="tile-sub">Morbi diam mauris viverra in gravida</div>
  </div>
  <div class="tile tile-cyan">
    <div class="tile-photo" role="img" aria-label="Worker packing cartons on a conveyor, blue tint"></div>
    <svg class="tile-hex" width="84" height="94" viewBox="0 0 84 94"><polygon points="42,2 82,24 82,70 42,92 2,70 2,24" fill="#fff"/><g fill="var(--tile-cyan)"><rect x="36" y="30" width="12" height="10"/><rect x="22" y="54" width="12" height="10"/><rect x="36" y="54" width="12" height="10"/><rect x="50" y="54" width="12" height="10"/><rect x="40.5" y="40" width="3" height="14"/><rect x="27" y="46" width="30" height="2.5"/><rect x="27" y="46" width="2.5" height="8"/><rect x="54.5" y="46" width="2.5" height="8"/></g></svg>
    <div class="tile-title">Build</div>
    <div class="tile-sub">Morbi diam mauris viverra in gravida</div>
  </div>
  <div class="tile tile-navy">
    <div class="tile-photo" role="img" aria-label="Smiling colleague at the office, navy tint"></div>
    <svg class="tile-hex" width="84" height="94" viewBox="0 0 84 94"><polygon points="42,2 82,24 82,70 42,92 2,70 2,24" fill="#fff"/><g fill="var(--tile-navy)"><polygon points="42,30 52,35 42,40 32,35"/><polygon points="31,37 41,42 41,52 31,47"/><polygon points="43,42 53,37 53,47 43,52"/><polygon points="31,50 41,55 41,65 31,60"/><polygon points="20,44 30,49 30,59 20,54"/><polygon points="43,55 53,50 53,60 43,65"/><polygon points="55,49 65,44 65,54 55,59"/></g></svg>
    <div class="tile-title">Our Work</div>
    <div class="tile-sub">Morbi diam mauris viverra in gravida</div>
  </div>
</section>

<section class="benefits abs">
  <div class="benefit-block" style="left:140px">
    <h2 class="benefit-heading orange">Major Benefits</h2>
  </div>
  <div class="benefit-photo" style="left:141px;top:104px;width:181px;height:178px;background:linear-gradient(135deg,#b98a55,#d9c3a2 50%,#6c7a8e)" role="img" aria-label="Warehouse worker in a hard hat using a tablet between shelves"></div>
  <ul class="benefit-list" style="left:338px;top:104px;width:280px">
    <li>Inventory accuracy and tracking throught the warehouse</li>
    <li>Barcoding and loctaion tracking</li>
    <li>Picking and receiving efficiencies</li>
    <li>Strengthen order fulfillment precision</li>
    <li>Imporve customer satisfaction</li>
    <li>Reduce Labor Costs</li>
  </ul>
  <div class="benefit-block" style="left:644px">
    <h2 class="benefit-heading cyan">Key Features</h2>
  </div>
  <div class="benefit-photo" style="left:645px;top:104px;width:181px;height:178px;background:linear-gradient(135deg,#c27a3a,#8a7f78 50%,#3f5a78)" role="img" aria-label="Worker in a hard hat using a laptop in a warehouse aisle"></div>
  <ul class="benefit-list" style="left:846px;top:100px;width:300px">
    <li>Lot traceability and recall</li>
    <li>Returns, damage and recoup</li>
    <li>Messaging and tax engine</li>
    <li>Price History and pricing engine</li>
    <li>Vendor Portal</li>
    <li>Dashboard, reporting and analytics</li>
  </ul>
</section>

<footer class="site-footer abs">
  <div class="footer-col" style="left:143px">
    <h3>COMPANY</h3>
    <ul><li>About Us</li><li>What We Do</li><li>Why Choose Us</li><li>Solutions</li><li>Hire Us</li></ul>
  </div>
  <div class="footer-col" style="left:315px">
    <h3>SERVICES</h3>
    <ul><li>Morbi diam</li><li>Aauris viverra</li><li>Gravida mattis</li><li>Sonummy nibh ligula</li><li>pulvinar metus</li></ul>
  </div>
  <div class="footer-col" style="left:519px">
    <h3>NEWSLETTER SIGN UP</h3>
    <p class="newsletter-note">Mauris vel lacus vitae felis vestibulum</p>
    <div class="email-field">Email address</div>
    <div class="subscribe-btn">SUBSCRIBE</div>
  </div>
  <div class="footer-col" style="left:826px">
    <h3>CONTACT US</h3>
    <div class="contact-lines">48 Harlow Bend #4B<br>Ferndale 75301 TX<br>555.017.3864<br>info@marvetrix.com</div>
    <div class="social"><span></span><span></span><span></span><span></span></div>
  </div>
</footer>
<div class="footer-bottom abs"><p>© 2015 Company Name &nbsp;All right reserved &nbsp;Term of Use</p></div>

</body>
</html>
```